Stationary and Business Card Design

We need a stationery design and a business card design for a non-profit economics development agency. Our website is growharborline.org. Our clients are Canadian government agencies and large Chinese company. We need the design to be professional and corporate.

Please see attached for our Power Point presentation. Please take design elements from our website and our ppt.

```html
<!DOCTYPE html>
<html lang="en">
<head>
<meta charset="utf-8">
<title>Harborline Growth Alliance — Stationery Set</title>
<link rel="stylesheet" href="https://fonts.googleapis.com/css2?family=Arimo:wght@400;700&family=Didact+Gothic&display=swap">
<style>
  :root {
    --brand-red: #e8303a;
    --ink: #1a1a1a;
    --band: #1e1e1e;
    --paper: #ffffff;
    --muted: #555555;
    --bg-deep: #6e0006;
    --bg-bright: #b5121b;
    --sans: "Arimo", Arial, sans-serif;
    --url: "Didact Gothic", "Century Gothic", sans-serif;
  }
  * { box-sizing: border-box; margin: 0; padding: 0; }
  html, body { width: 1200px; height: 780px; overflow: hidden; }
  body {
    position: relative;
    font-family: var(--sans);
    color: var(--ink);
    background: radial-gradient(ellipse at 75% 10%, var(--bg-bright), var(--bg-deep) 75%);
  }
  .sheet, .card, .envelope {
    position: absolute;
    background: var(--paper);
    box-shadow: 0 8px 22px rgba(0,0,0,.35);
    overflow: hidden;
  }

  /* Brand name lockup */
  .brand { display: flex; align-items: center; gap: 6px; font-weight: 700; color: var(--brand-red); white-space: nowrap; }
  .brand-square { width: 12px; height: 12px; background: var(--brand-red); flex: none; }
  .brand--light { color: var(--paper); }
  .brand--light .brand-square { background: var(--paper); }

  /* Footer band with web address */
  .footer-band {
    position: absolute; left: 0; right: 0; bottom: 0;
    background: var(--band);
    border-top: 4px solid var(--brand-red);
    color: #e6e6e6;
    font-family: var(--url);
    text-align: center;
    letter-spacing: .32em;
  }

  /* Letterhead */
  .sheet { width: 360px; height: 470px; }
  .sheet--back { left: 150px; top: 120px; }
  .sheet--front { left: 60px; top: 200px; }
  .sheet .brand { position: absolute; left: 28px; top: 30px; font-size: 11px; }
  .sheet-contact { position: absolute; right: 26px; top: 28px; font-size: 7px; line-height: 11px; color: var(--muted); }
  .sheet-contact li { list-style: none; display: flex; align-items: center; gap: 4px; }
  .sheet-contact svg { width: 7px; height: 7px; fill: var(--ink); }
  .sheet-rule { position: absolute; left: 28px; right: 26px; top: 58px; height: 1px; background: #bbb; }
  .letter { position: absolute; left: 28px; right: 30px; top: 86px; font-size: 7.6px; line-height: 10.5px; }
  .letter p { margin-bottom: 10px; }
  .signature { margin-top: 26px; width: 140px; border-top: 1px solid var(--ink); padding-top: 4px; }
  .signature strong { display: block; font-size: 9px; }
  .signature span { font-size: 8px; color: var(--muted); }
  .sheet .footer-band { height: 40px; line-height: 36px; font-size: 9px; }

  /* Business cards */
  .card { width: 240px; height: 140px; }
  .card--front-a { left: 560px; top: 110px; }
  .card--back-a { left: 830px; top: 110px; }
  .card--back-b { left: 560px; top: 270px; }
  .card--front-b { left: 830px; top: 270px; }
  .card-panel {
    position: absolute; left: 0; top: 0; bottom: 0; width: 108px;
    background: var(--brand-red); padding: 20px 12px;
  }
  .card-panel .brand { font-size: 8px; }
  .card-panel .card-url { position: absolute; left: 12px; bottom: 14px; font-family: var(--url); font-size: 7px; letter-spacing: .12em; color: #ffe3e4; }
  .card-person { position: absolute; left: 122px; top: 20px; }
  .card-person strong { display: block; font-size: 10px; }
  .card-person span { font-size: 7px; color: var(--muted); }
  .card-details { position: absolute; left: 122px; top: 66px; font-size: 6.5px; line-height: 10px; color: var(--muted); list-style: none; }
  .card-details li { display: flex; align-items: center; gap: 4px; }
  .card-details svg { width: 6px; height: 6px; fill: var(--ink); }
  .card .brand--centered { position: absolute; left: 24px; top: 44px; font-size: 12px; }
  .card .footer-band { height: 24px; line-height: 20px; font-size: 8px; }

  /* Envelope */
  .envelope { left: 560px; top: 440px; width: 560px; height: 250px; }
  .envelope .brand { position: absolute; left: 28px; top: 30px; font-size: 13px; }
  .envelope .footer-band { height: 42px; line-height: 38px; font-size: 11px; }
</style>
</head>
<body>

<svg width="0" height="0" style="position:absolute" aria-hidden="true">
  <symbol id="icon-phone" viewBox="0 0 10 10"><path d="M2 0h2l1 3-1.5 1a6 6 0 0 0 2.5 2.5L7 5l3 1v2c0 1-1 2-2 2A8 8 0 0 1 0 2c0-1 1-2 2-2z"/></symbol>
  <symbol id="icon-mail" viewBox="0 0 10 10"><path d="M0 2h10v6H0z M0 2l5 3.5L10 2" fill-opacity="1"/></symbol>
  <symbol id="icon-fax" viewBox="0 0 10 10"><path d="M2 0h6v3H2z M0 4h10v6H0z"/></symbol>
</svg>

<!-- Letterhead, second page -->
<section class="sheet sheet--back" aria-label="Letterhead second sheet">
  <div class="brand"><span class="brand-square"></span>Harborline Growth Alliance</div>
  <ul class="sheet-contact">
    <li><svg><use href="#icon-phone"/></svg>555 014 2290</li>
    <li><svg><use href="#icon-mail"/></svg>info@growharborline.org</li>
  </ul>
  <div class="sheet-rule"></div>
  <div class="footer-band">www.growharborline.org</div>
</section>

<!-- Letterhead, first page -->
<section class="sheet sheet--front" aria-label="Letterhead">
  <div class="brand"><span class="brand-square"></span>Harborline Growth Alliance</div>
  <ul class="sheet-contact">
    <li><svg><use href="#icon-phone"/></svg>555 014 2290</li>
    <li><svg><use href="#icon-mail"/></svg>info@growharborline.org</li>
  </ul>
  <div class="letter">
    <p>Greetings!</p>
    <p>Lorem ipsum dolor sit amet, consectetur adipisicing elit, sed do eiusmod tempor incididunt ut labore et dolore magna aliqua. Ut enim ad minim veniam, quis nostrud exercitation ullamco laboris nisi ut aliquip ex ea commodo consequat. Duis aute irure dolor in reprehenderit in voluptate velit esse cillum dolore eu fugiat nulla pariatur. Excepteur sint occaecat cupidatat non proident, sunt in culpa qui officia deserunt mollit anim id est laborum.</p>
    <p>At vero eos et accusamus et iusto odio dignissimos ducimus qui blanditiis praesentium voluptatum deleniti atque corrupti quos dolores et quas molestias excepturi sint occaecati cupiditate non provident, similique sunt in culpa qui officia deserunt mollitia animi, id est laborum et dolorum fuga. Et harum quidem rerum facilis est et expedita distinctio. Nam libero tempore, cum soluta nobis est eligendi optio cumque nihil impedit quo minus id quod maxime placeat facere possimus, omnis voluptas assumenda est, omnis dolor repellendus.</p>
    <p>Sincerely,</p>
    <div class="signature">
      <strong>Given Name M. Surname</strong>
      <span>Position/Designation</span>
    </div>
  </div>
  <div class="footer-band">www.growharborline.org</div>
</section>

<!-- Business card, front -->
<article class="card card--front-a" aria-label="Business card front">
  <div class="card-panel">
    <div class="brand brand--light"><span class="brand-square"></span>Harborline Growth<br>Alliance</div>
    <div class="card-url">growharborline.org</div>
  </div>
  <div class="card-person"><strong>Alex Moreau</strong><span>Position/Title</span></div>
  <ul class="card-details">
    <li><svg><use href="#icon-mail"/></svg>alex@growharborline.org</li>
    <li><svg><use href="#icon-phone"/></svg>+1 555 014 2290</li>
    <li><svg><use href="#icon-phone"/></svg>+1 555 014 2291</li>
    <li><svg><use href="#icon-fax"/></svg>+1 555 014 2292</li>
  </ul>
</article>

<!-- Business card, back -->
<article class="card card--back-a" aria-label="Business card back">
  <div class="brand brand--centered"><span class="brand-square"></span>Harborline Growth Alliance</div>
  <div class="footer-band">www.growharborline.org</div>
</article>

<article class="card card--back-b" aria-label="Business card back">
  <div class="brand brand--centered"><span class="brand-square"></span>Harborline Growth Alliance</div>
  <div class="footer-band">www.growharborline.org</div>
</article>

<article class="card card--front-b" aria-label="Business card front">
  <div class="card-panel">
    <div class="brand brand--light"><span class="brand-square"></span>Harborline Growth<br>Alliance</div>
    <div class="card-url">growharborline.org</div>
  </div>
  <div class="card-person"><strong>Alex Moreau</strong><span>Position/Title</span></div>
  <ul class="card-details">
    <li><svg><use href="#icon-mail"/></svg>alex@growharborline.org</li>
    <li><svg><use href="#icon-phone"/></svg>+1 555 014 2290</li>
    <li><svg><use href="#icon-phone"/></svg>+1 555 014 2291</li>
    <li><svg><use href="#icon-fax"/></svg>+1 555 014 2292</li>
  </ul>
</article>

<!-- Envelope -->
<section class="envelope" aria-label="Envelope">
  <div class="brand"><span class="brand-square"></span>Harborline Growth Alliance</div>
  <div class="footer-band">www.growharborline.org</div>
</section>

</body>
</html>
```